Vantolo Entertainment - Website
Production House + Creative Agency
Project: Vantolo Entertainment - Website
Vantolo Entertainment - Website - Entertainment
Creative Brief
Entertainment
http://myvantolo-example.com
We are looking for a clean, professional, easy to use website for our fans and potential business partners. There are three facets of our business:
1) Entertainment: record label, industry interviews, and production house for film
2) Creative: advertising agency and music publishing catalogue
3) Enterprises (name subject to change): our partner-site, where affiliates can log in, keep track of their earnings, and get product training
Service Oriented
Royal Purple
Grey
Golden Yellow possibly
left side
We envision a splash page with our three businesses, and the visitor is directed to whichever they are interested in (we would track the clicks to determine where our customers/partners/fans are going). For all the other pages, we were playing with the idea of navigation on the left hand side as opposed to the top. Icon based navigation, like app icons on iphones, perhaps? We're interested to see what you can dream up for this. On the Entertainment page, we require sections for: - Music (soundcloud links that use the album/single cover as the icon) to listen to - link to the mixtape of the week and radio podcasts at the very top - Videos of our artists, trailers, etc.. - Industry news, like an RSS feed - Link to our "Idea Forge" section, which is a collection of interviews with industry professionals (was thinking a stylized quote, with a read more link) - artist page template that features a quick bio, with links to the catalog for more songs On the Creative Page we require: - a catalog page, which can be sorted by style or artist - samples of our advertising work - list of our services - featured crew member of the month On our Enterprises page, it should essentially be a dashboard with their account information, more information on their earnings and what they are authorized to sell. Additionally, we'd like to see: - a calendar with available dates they can book - premium content from the "Idea Forge" sessions for our member's only - music licensing of the week - featured song/artist section which they can sell to other agencies to make money As for the three main page templates, they should all use the same colour theme - but maybe some slight tweaking to indicate it is a different section of the site. Perhaps a tertiary colour that changes between the three pages (purple and black are used on all pages, but then gold, silver, and bronze are used on separate pages, respectively. This is an idea to use.

```html
<!DOCTYPE html>
<html lang="en">
<head>
<meta charset="utf-8">
<title>Vantolo Entertainment – Entertainment</title>
<link href="https://fonts.googleapis.com/css2?family=Cinzel:wght@400;700&family=Crimson+Text:wght@400;600&display=swap" rel="stylesheet">
<style>
:root{
  --purple-deep:#3a0f4f;
  --purple:#6a2585;
  --purple-light:#a04fb8;
  --magenta:#b640a8;
  --gold:#e6b84a;
  --gold-light:#f7df8a;
  --gold-dark:#a57a24;
  --green-band:#5a8a2a;
  --grey:#8c8c8c;
  --grey-dark:#4a4a4a;
  --panel:#2a0a35;
  --stage-dark:#0e1024;
  --stage-blue:#2c4f9a;
  --stage-teal:#2aa6b8;
  --stage-red:#c2402c;
  --stage-violet:#5a2a7a;
  --white:#ffffff;
}
*{box-sizing:border-box;margin:0;padding:0}
html,body{width:1200px;height:901px;overflow:hidden;background:var(--purple-deep)}
.page{position:relative;width:1200px;height:901px;overflow:hidden;
  background:linear-gradient(180deg,var(--purple) 0%,var(--magenta) 45%,var(--purple) 75%,var(--purple-deep) 100%);
  font-family:'Crimson Text',serif;color:var(--white)}
.top-band{position:absolute;left:0;top:0;width:1200px;height:20px;
  background:linear-gradient(180deg,var(--gold-light),var(--gold) 45%,var(--green-band) 100%)}
.header{position:absolute;left:0;top:20px;width:1200px;height:200px;
  background:linear-gradient(160deg,var(--purple-light) 0%,var(--purple) 40%,var(--magenta) 70%,var(--purple-light) 100%)}
.brand{position:absolute;left:20px;top:36px;width:290px;text-align:center}
.brand-mark{display:block;width:80px;height:80px;margin:0 auto 22px;background:var(--white)}
.brand-name{font-family:'Cinzel',serif;font-size:21px;letter-spacing:.5px;color:var(--white);white-space:nowrap}
.section-title{position:absolute;left:360px;top:125px;width:480px;text-align:center;
  font-family:'Cinzel',serif;font-weight:400;font-size:54px;line-height:1;color:var(--gold);letter-spacing:1px;white-space:nowrap}
.utility-icons{position:absolute;right:20px;top:38px;display:flex;gap:14px}
.utility-icons svg{width:18px;height:18px}
.search{position:absolute;left:791px;top:84px;width:330px;height:42px;border-radius:4px;
  background:linear-gradient(180deg,#f4f0f6,#cfc6d4)}
.search-btn{position:absolute;left:1130px;top:82px;width:48px;height:48px}
.social{position:absolute;left:940px;top:142px;display:flex;gap:4px}
.social span{width:26px;height:26px;border-radius:4px;display:block}
.social .s1{background:#e07a22}.social .s2{background:#e0a022}.social .s3{background:#3b5ca0}.social .s4{background:#3b5ca0}.social .s5{background:#c9b07a}
.fans{position:absolute;left:1102px;top:134px;width:62px;height:74px;border:2px solid var(--gold-light);border-radius:4px;
  background:linear-gradient(180deg,var(--gold-light),var(--gold-dark));text-align:center;
  font-family:'Cinzel',serif;font-size:13px;color:var(--purple-deep);padding-top:4px}
.fans svg{width:44px;height:44px;display:block;margin:0 auto}
.sidebar{position:absolute;left:0;top:220px;width:146px;height:681px;
  background:linear-gradient(90deg,var(--gold-dark),var(--gold-light) 50%,var(--gold) 100%)}
.nav-item{position:absolute;left:14px;width:120px;font-family:'Cinzel',serif;font-size:11px;line-height:1.15;color:var(--white);
  text-shadow:0 1px 1px rgba(0,0,0,.45)}
.nav-icon{width:48px;height:46px;margin-bottom:4px;border-radius:4px;
  background:linear-gradient(180deg,#c8c8c8,var(--grey));display:flex;align-items:center;justify-content:center}
.nav-icon svg{width:30px;height:30px}
.nav-item.active .nav-icon{background:linear-gradient(180deg,#a8a8a8,var(--grey-dark))}
.hero{position:absolute;left:165px;top:231px;width:1008px;height:407px;border:3px solid #cfc6d4;
  background:
    radial-gradient(ellipse 180px 140px at 82% 42%,rgba(42,166,184,.75),transparent 70%),
    radial-gradient(ellipse 160px 220px at 94% 60%,rgba(44,79,154,.8),transparent 70%),
    radial-gradient(ellipse 220px 200px at 30% 48%,rgba(194,64,44,.85),transparent 70%),
    radial-gradient(ellipse 300px 120px at 45% 82%,rgba(90,42,122,.8),transparent 70%),
    linear-gradient(135deg,var(--stage-blue) 0%,var(--stage-dark) 45%,var(--stage-violet) 100%)}
.hero-arrow{position:absolute;top:12px;width:80px;height:80px}
.hero-arrow.prev{left:14px}.hero-arrow.next{right:14px}
.eq-bg{position:absolute;left:146px;top:638px;width:1054px;height:263px;
  background:linear-gradient(180deg,rgba(160,79,184,.35),rgba(58,15,79,.55))}
.panel{position:absolute;top:669px;width:385px;height:212px;border-radius:10px;
  background:var(--panel);border:2px solid #7a4d8a;padding:10px 34px 0 14px}
.panel.left{left:243px}.panel.right{left:700px}
.panel h2{font-family:'Crimson Text',serif;font-weight:400;font-size:31px;text-align:center;line-height:1;margin-bottom:8px;letter-spacing:.5px;white-space:nowrap}
.panel p{font-size:14.5px;line-height:1.13;text-align:center;height:148px;overflow:hidden}
.scrollbar{position:absolute;right:8px;top:14px;width:16px;height:184px;border-radius:3px;background:#d8d0dc}
.scrollbar .up,.scrollbar .down{position:absolute;left:2px;width:12px;height:12px;background:var(--grey-dark);border-radius:2px}
.scrollbar .up{top:3px}.scrollbar .down{bottom:3px}
</style>
</head>
<body>
<div class="page">
  <div class="top-band"></div>
  <header class="header">
    <div class="brand">
      <span class="brand-mark"></span>
      <div class="brand-name">Vantolo Entertainment LLC</div>
    </div>
    <div class="utility-icons">
      <svg viewBox="0 0 20 20"><path d="M2 10 L10 3 L18 10 M5 9 V17 H15 V9" fill="none" stroke="#fff" stroke-width="2"/></svg>
      <svg viewBox="0 0 20 20"><circle cx="10" cy="8" r="5" fill="#fff"/><rect x="8" y="13" width="4" height="5" fill="#fff"/></svg>
      <svg viewBox="0 0 20 20"><path d="M3 12 A7 7 0 0 1 17 12 V17 H13 V12 H17 M3 12 V17 H7 V12 H3" fill="#fff" stroke="#fff"/></svg>
      <svg viewBox="0 0 20 20"><rect x="2" y="4" width="16" height="12" fill="#fff"/></svg>
      <svg viewBox="0 0 20 20"><path d="M2 4 H18 V14 H8 L4 18 V14 H2 Z" fill="#fff"/></svg>
      <svg viewBox="0 0 20 20"><path d="M2 3 H5 L7 13 H16 L18 6 H6" fill="none" stroke="#fff" stroke-width="2"/><circle cx="8" cy="17" r="1.6" fill="#fff"/><circle cx="15" cy="17" r="1.6" fill="#fff"/></svg>
    </div>
    <h1 class="section-title">Entertainment</h1>
  </header>
  <div class="search"></div>
  <svg class="search-btn" viewBox="0 0 48 48"><circle cx="20" cy="20" r="12" fill="none" stroke="#fff" stroke-width="5"/><path d="M29 29 L42 42" stroke="#fff" stroke-width="6" stroke-linecap="round"/></svg>
  <div class="social"><span class="s1"></span><span class="s2"></span><span class="s3"></span><span class="s4"></span><span class="s5"></span></div>
  <div class="fans">
    <svg viewBox="0 0 24 24"><path d="M12 2 L15 9 L22 9.5 L16.5 14 L18.5 21 L12 17 L5.5 21 L7.5 14 L2 9.5 L9 9 Z" fill="var(--white)"/></svg>
    Fans
  </div>

  <nav class="sidebar">
    <div class="nav-item active" style="top:12px">
      <div class="nav-icon"><svg viewBox="0 0 30 30"><path d="M9 6 L24 15 L9 24 Z" fill="#fff"/></svg></div>Music
    </div>
    <div class="nav-item" style="top:86px">
      <div class="nav-icon"><svg viewBox="0 0 30 30"><path d="M24 15 A9 9 0 1 1 20 7" fill="none" stroke="#fff" stroke-width="4"/><path d="M17 3 L24 6 L19 12 Z" fill="#fff"/></svg></div>Mixtape of the week and radio
    </div>
    <div class="nav-item" style="top:188px">
      <div class="nav-icon"><svg viewBox="0 0 30 30"><rect x="3" y="10" width="17" height="13" fill="#fff"/><path d="M20 14 L27 10 V23 L20 19 Z" fill="#fff"/><circle cx="8" cy="7" r="3" fill="#fff"/><circle cx="15" cy="7" r="3" fill="#fff"/></svg></div>Video
    </div>
    <div class="nav-item" style="top:266px">
      <div class="nav-icon"><svg viewBox="0 0 30 30"><rect x="5" y="5" width="20" height="20" fill="#fff"/><path d="M8 10 H22 M8 14 H22 M8 18 H18" stroke="var(--grey)" stroke-width="2"/></svg></div>Industry news
    </div>
    <div class="nav-item" style="top:351px">
      <div class="nav-icon"><svg viewBox="0 0 30 30"><circle cx="15" cy="10" r="6" fill="#fff"/><path d="M4 27 Q15 12 26 27 Z" fill="#fff"/></svg></div>Idea Forge
    </div>
    <div class="nav-item" style="top:461px">
      <div class="nav-icon"><svg viewBox="0 0 30 30"><rect x="4" y="6" width="22" height="16" fill="#fff"/><rect x="10" y="23" width="10" height="3" fill="#fff"/></svg></div>Featured artists quick bio
    </div>
  </nav>

  <div class="hero" role="img" aria-label="Featured banner artwork: a DJ performing at turntables under blue and red club lights">
    <svg class="hero-arrow prev" viewBox="0 0 80 80"><path d="M60 8 L10 40 L60 72 Z" fill="rgba(255,255,255,.35)"/></svg>
    <svg class="hero-arrow next" viewBox="0 0 80 80"><path d="M20 8 L70 40 L20 72 Z" fill="rgba(255,255,255,.35)"/></svg>
  </div>

  <div class="eq-bg" role="img" aria-label="Decorative equalizer bars background"></div>

  <section class="panel left">
    <h2>NEW THIS WEEK</h2>
    <p>Stream the mixtape of the week and catch up on our latest radio podcasts, hand-picked by the Vantolo crew. Fresh singles from our label artists drop every Friday, with exclusive studio sessions, remixes and behind-the-scenes stories. Tap any cover in the Music section to listen, share your favourite tracks with friends, and follow our artists for tour dates, new videos and release news all year long.</p>
    <div class="scrollbar"><span class="up"></span><span class="down"></span></div>
  </section>
  <section class="panel right">
    <h2>INDUSTRY NEWS</h2>
    <p>Interviews, releases and headlines from across the music and film business, updated daily. Read conversations with producers, managers and directors in the Idea Forge, see trailers from our production house, and find out which artists are heading into the studio next. Subscribe to the news feed to get every story first, and check back often for features on the people shaping the industry today.</p>
    <div class="scrollbar"><span class="up"></span><span class="down"></span></div>
  </section>
</div>
</body>
</html>
```